Updated Business Card Design more modern and eye catching

looking for something more dynamic than the sterile card we have now. Please take a look at our web site www.quarvinstores.net to see what we do. only looking for the front side of the card for now. I've also attached a sample of a card with raised spot uv ink - it might be cool to incorporate something like that. Card should be bold yet serious. No frilly or scrolly stuff on it.
Updates
Target Market(s)
We do decor and signage for retail business and supermarkets. Our new name should reflect that we're hip but serious.
Contact Information for Business Card
standard business card size - horizontal preferred
Font styles to use
Requirements
Must have
- Current logo and colors cannot be changed.
Nice to have
- Must have information shown on existing card but open to some changes. Okay to consider spot uv.
Should not have
- Not busy with pictures in the background.

```html
<!DOCTYPE html>
<html lang="en">
<head>
<meta charset="utf-8">
<title>Quarvin Stores – Business Card</title>
<link href="https://fonts.googleapis.com/css2?family=Exo+2:wght@400;500;600&display=swap" rel="stylesheet">
<style>
  :root{
    --backdrop:#f799b1;
    --ink:#0b0b0b;
    --paper:#f4f4f2;
    --gold:#b3a45a;
    --lime:#a3b82c;
    --text:#1a1a1a;
  }
  *{box-sizing:border-box;margin:0;padding:0}
  html,body{width:1200px;height:1166px;overflow:hidden}
  body{background:var(--backdrop);font-family:"Exo 2",sans-serif;position:relative}
  .card{position:absolute;left:250px;width:700px;height:400px;box-shadow:0 10px 24px rgba(120,30,60,.25)}
  .card-back{top:140px;background:var(--ink)}
  .card-front{top:630px;background:var(--paper)}
  .brand{position:absolute;display:flex;align-items:center;gap:22px}
  .brand-square{width:54px;height:54px;border:3px solid var(--gold)}
  .brand-name{font-weight:500;font-size:54px;letter-spacing:4px;color:var(--gold);text-transform:uppercase;line-height:1}
  .card-back .brand{left:50%;top:50%;transform:translate(-50%,-50%)}
  .card-front .brand{left:64px;top:58px}
  .card-front .brand-name{font-size:46px}
  .card-front .brand-square{width:46px;height:46px}
  .edge-mark{position:absolute;left:0;top:216px;width:30px}
  .edge-mark span{display:block;height:38px;background:var(--lime)}
  .edge-mark span+span{height:14px;background:var(--ink)}
  .person{position:absolute;left:64px;top:200px}
  .person-name{font-size:34px;font-weight:600;color:var(--lime);line-height:1}
  .person-title{font-size:15px;color:var(--text);margin-top:4px;padding-left:14px}
  .contact-list{position:absolute;left:64px;top:268px;list-style:none}
  .contact-list li{display:flex;align-items:center;gap:14px;font-size:19px;color:var(--text);height:27px}
  .contact-list svg{width:18px;height:18px;flex:none}
  .address{position:absolute;right:48px;top:232px;text-align:right;font-size:19px;color:var(--text);line-height:1.3}
</style>
</head>
<body>
  <section class="card card-back" aria-label="Card back">
    <div class="brand"><span class="brand-square"></span><span class="brand-name">Quarvin Stores</span></div>
  </section>

  <section class="card card-front" aria-label="Card front">
    <div class="brand"><span class="brand-square"></span><span class="brand-name">Quarvin Stores</span></div>
    <div class="edge-mark"><span></span><span></span></div>
    <div class="person">
      <p class="person-name">Maren Talbot</p>
      <p class="person-title">Vice-President</p>
    </div>
    <ul class="contact-list">
      <li><svg viewBox="0 0 18 18" fill="none" stroke="var(--lime)" stroke-width="1.6"><rect x="5" y="1.5" width="8" height="15" rx="1.5"/><line x1="8" y1="14" x2="10" y2="14"/></svg>(555) 014-2286</li>
      <li><svg viewBox="0 0 18 18" fill="none" stroke="var(--lime)" stroke-width="1.6"><path d="M2 6c0-2 3-3 7-3s7 1 7 3l-3 1-1-2H6L5 7z"/><rect x="4" y="9" width="10" height="7" rx="1"/><circle cx="9" cy="12.5" r="1.6"/></svg>(555) 017-3390 ext.3</li>
      <li><svg viewBox="0 0 18 18"><rect x="1.5" y="4" width="15" height="10" rx="1" fill="var(--lime)"/><path d="M2 5l7 5 7-5" fill="none" stroke="var(--paper)" stroke-width="1.4"/></svg>maren@quarvinstores.net</li>
      <li><svg viewBox="0 0 18 18" fill="none" stroke="var(--lime)" stroke-width="1.6"><circle cx="9" cy="9" r="7"/><ellipse cx="9" cy="9" rx="3" ry="7"/><line x1="2" y1="9" x2="16" y2="9"/></svg>www.quarvinstores.net</li>
    </ul>
    <p class="address">4410 Harbor Commerce Way<br>Lakeview Bay, FL 30217</p>
  </section>
</body>
</html>
```